Ridgeline Haulage Business Card Design

We are a new company base in Far North Queensland Australia called Ridgeline Haulage. We are a company that hire machinery (graders, rollers, excavators and trucks) for road construction and earthworks. We also supply quarry products to the building and construction industries. (Crushed aggregates, road base materials, sand, gravel and rocks). Would like a logo that can also be used on our plant to advertise us.
Target Market(s)
engineers, builders and general public
Industry/Entity Type
Construction
Contact Information for Business Card
Ridgeline Haulage Pty Ltd, Dale and Merryn Vosper
ABN: 38 502 716 904 ACN: 502 716 904
PO Box 19, Marrabee Qld 4871
Pardalote Street Marrabee Qld 4871

```html
<!DOCTYPE html>
<html lang="en">
<head>
<meta charset="utf-8">
<title>Ridgeline Haulage Business Card</title>
<link rel="stylesheet" href="https://fonts.googleapis.com/css2?family=Source+Sans+3:wght@400;600;700&display=swap">
<style>
  :root {
    --page: #ffffff;
    --card-blue: #2d4f98;
    --card-blue-deep: #26458a;
    --brand-green: #8cc152;
    --name-gold: #f2b632;
    --text-white: #ffffff;
    --shadow: rgba(0, 0, 0, 0.55);
  }
  html, body {
    margin: 0;
    padding: 0;
    width: 1200px;
    height: 741px;
    overflow: hidden;
    background: var(--page);
    font-family: "Source Sans 3", sans-serif;
  }
  .card {
    position: absolute;
    left: 42px;
    top: 39px;
    width: 1113px;
    height: 656px;
    background: radial-gradient(ellipse at center, var(--card-blue) 0%, var(--card-blue-deep) 100%);
    color: var(--text-white);
    text-align: center;
  }
  .company-title {
    position: absolute;
    left: 0;
    right: 0;
    top: 30px;
    margin: 0;
    font-size: 68px;
    font-weight: 600;
    line-height: 1;
    letter-spacing: -0.5px;
    text-shadow: 2px 3px 4px var(--shadow);
  }
  .company-title .place { color: var(--brand-green); }
  .company-title .trade { color: var(--text-white); }
  .brand-mark {
    position: absolute;
    left: 0;
    right: 0;
    top: 206px;
    display: flex;
    align-items: center;
    justify-content: center;
    gap: 16px;
  }
  .brand-mark .dot {
    width: 46px;
    height: 46px;
    border-radius: 50%;
    background: var(--brand-green);
  }
  .brand-mark .name {
    font-size: 34px;
    font-weight: 600;
    color: var(--brand-green);
  }
  .owners {
    position: absolute;
    left: 0;
    right: 0;
    top: 358px;
    margin: 0;
    font-size: 54px;
    font-weight: 700;
    line-height: 1;
    letter-spacing: -0.5px;
    color: var(--name-gold);
    text-shadow: 2px 3px 4px var(--shadow);
  }
  .details {
    position: absolute;
    left: 0;
    right: 0;
    top: 424px;
    margin: 0;
    padding: 0;
    list-style: none;
    font-size: 35px;
    font-weight: 400;
    line-height: 49.5px;
  }
</style>
</head>
<body>
  <section class="card">
    <h1 class="company-title"><span class="place">Ridgeline</span><span class="trade">Haulage Pvt.Ltd</span></h1>
    <div class="brand-mark">
      <span class="dot"></span>
      <span class="name">Ridgeline Haulage</span>
    </div>
    <h2 class="owners">Dale and Merryn Vosper</h2>
    <ul class="details">
      <li>ABN: 38 502 716 904</li>
      <li>ACN: 502 716 904</li>
      <li>PO Box 19, Marrabee Qld 4871</li>
      <li>Pardalote Street Marrabee Qld 4871</li>
    </ul>
  </section>
</body>
</html>
```